Step and Repeat Backdrop for wedding reception photo booth

Would like to have a Step and Repeat Backdrop (8 foot high by 10 foot wide) that incorporates the wedding logo (attached) and the names Elena and Gavin. Background should be white, and wedding colors are burgundy and gold. Show me creativity :-) I have included some random samples.

```html
<!DOCTYPE html>
<html lang="en">
<head>
<meta charset="utf-8">
<title>Elena &amp; Gavin — Step and Repeat Backdrop</title>
<link rel="stylesheet" href="https://fonts.googleapis.com/css2?family=Cormorant+Garamond:wght@600&display=swap">
<style>
  :root {
    --backdrop: #ffffff;
    --burgundy: #551416;
    --ornament-tint: rgba(85, 20, 22, 0.22);
  }
  * { margin: 0; padding: 0; box-sizing: border-box; }
  html, body {
    width: 1200px;
    height: 943px;
    overflow: hidden;
    background: var(--backdrop);
  }
  .backdrop {
    position: relative;
    width: 1200px;
    height: 943px;
    background: var(--backdrop);
  }
  .crest {
    position: absolute;
    display: flex;
    flex-direction: column;
    align-items: center;
    transform: translate(-50%, -50%);
    gap: 4px;
  }
  .flourish {
    display: block;
    background: var(--ornament-tint);
    border-radius: 40% 40% 50% 50% / 60% 60% 40% 40%;
  }
  .crest .flourish { width: 96px; height: 26px; }
  .crest .flourish.lower { border-radius: 50% 50% 40% 40% / 40% 40% 60% 60%; }
  .initials {
    font-family: "Cormorant Garamond", serif;
    font-weight: 600;
    color: var(--burgundy);
    line-height: 0.9;
    letter-spacing: -1px;
  }
  .crest .initials { font-size: 50px; }
  .crest.small .flourish { width: 82px; height: 22px; }
  .crest.small .initials { font-size: 42px; }
  .crest.feature { gap: 10px; }
  .crest.feature .flourish { width: 250px; height: 64px; }
  .crest.feature .initials { font-size: 128px; letter-spacing: -3px; }
  .divider {
    position: absolute;
    transform: translate(-50%, -50%);
    width: 250px;
    height: 56px;
  }
</style>
</head>
<body>
<main class="backdrop">
  <!-- left columns -->
  <div class="crest" style="left:120px;top:110px"><span class="flourish" role="img" aria-label="scroll flourish ornament"></span><span class="initials">E&amp;G</span><span class="flourish lower" role="img" aria-label="scroll flourish ornament"></span></div>
  <div class="crest" style="left:120px;top:290px"><span class="flourish" role="img" aria-label="scroll flourish ornament"></span><span class="initials">E&amp;G</span><span class="flourish lower" role="img" aria-label="scroll flourish ornament"></span></div>
  <div class="crest" style="left:120px;top:470px"><span class="flourish" role="img" aria-label="scroll flourish ornament"></span><span class="initials">E&amp;G</span><span class="flourish lower" role="img" aria-label="scroll flourish ornament"></span></div>
  <div class="crest" style="left:120px;top:650px"><span class="flourish" role="img" aria-label="scroll flourish ornament"></span><span class="initials">E&amp;G</span><span class="flourish lower" role="img" aria-label="scroll flourish ornament"></span></div>
  <div class="crest" style="left:120px;top:830px"><span class="flourish" role="img" aria-label="scroll flourish ornament"></span><span class="initials">E&amp;G</span><span class="flourish lower" role="img" aria-label="scroll flourish ornament"></span></div>

  <div class="crest" style="left:340px;top:110px"><span class="flourish" role="img" aria-label="scroll flourish ornament"></span><span class="initials">E&amp;G</span><span class="flourish lower" role="img" aria-label="scroll flourish ornament"></span></div>
  <div class="crest" style="left:340px;top:290px"><span class="flourish" role="img" aria-label="scroll flourish ornament"></span><span class="initials">E&amp;G</span><span class="flourish lower" role="img" aria-label="scroll flourish ornament"></span></div>
  <div class="crest" style="left:340px;top:470px"><span class="flourish" role="img" aria-label="scroll flourish ornament"></span><span class="initials">E&amp;G</span><span class="flourish lower" role="img" aria-label="scroll flourish ornament"></span></div>
  <div class="crest" style="left:340px;top:650px"><span class="flourish" role="img" aria-label="scroll flourish ornament"></span><span class="initials">E&amp;G</span><span class="flourish lower" role="img" aria-label="scroll flourish ornament"></span></div>
  <div class="crest" style="left:340px;top:830px"><span class="flourish" role="img" aria-label="scroll flourish ornament"></span><span class="initials">E&amp;G</span><span class="flourish lower" role="img" aria-label="scroll flourish ornament"></span></div>

  <!-- centre column -->
  <span class="divider flourish" style="left:600px;top:90px" role="img" aria-label="ornamental scroll divider with fleur-de-lis"></span>
  <div class="crest small" style="left:600px;top:250px"><span class="flourish" role="img" aria-label="scroll flourish ornament"></span><span class="initials">E&amp;G</span><span class="flourish lower" role="img" aria-label="scroll flourish ornament"></span></div>
  <div class="crest feature" style="left:600px;top:470px"><span class="flourish" role="img" aria-label="large scroll flourish with fleur-de-lis"></span><span class="initials">E&amp;G</span><span class="flourish lower" role="img" aria-label="large scroll flourish with fleur-de-lis"></span></div>
  <div class="crest small" style="left:600px;top:690px"><span class="flourish" role="img" aria-label="scroll flourish ornament"></span><span class="initials">E&amp;G</span><span class="flourish lower" role="img" aria-label="scroll flourish ornament"></span></div>
  <span class="divider flourish lower" style="left:600px;top:855px" role="img" aria-label="ornamental scroll divider with fleur-de-lis"></span>

  <!-- right columns -->
  <div class="crest" style="left:860px;top:110px"><span class="flourish" role="img" aria-label="scroll flourish ornament"></span><span class="initials">E&amp;G</span><span class="flourish lower" role="img" aria-label="scroll flourish ornament"></span></div>
  <div class="crest" style="left:860px;top:290px"><span class="flourish" role="img" aria-label="scroll flourish ornament"></span><span class="initials">E&amp;G</span><span class="flourish lower" role="img" aria-label="scroll flourish ornament"></span></div>
  <div class="crest" style="left:860px;top:470px"><span class="flourish" role="img" aria-label="scroll flourish ornament"></span><span class="initials">E&amp;G</span><span class="flourish lower" role="img" aria-label="scroll flourish ornament"></span></div>
  <div class="crest" style="left:860px;top:650px"><span class="flourish" role="img" aria-label="scroll flourish ornament"></span><span class="initials">E&amp;G</span><span class="flourish lower" role="img" aria-label="scroll flourish ornament"></span></div>
  <div class="crest" style="left:860px;top:830px"><span class="flourish" role="img" aria-label="scroll flourish ornament"></span><span class="initials">E&amp;G</span><span class="flourish lower" role="img" aria-label="scroll flourish ornament"></span></div>

  <div class="crest" style="left:1080px;top:110px"><span class="flourish" role="img" aria-label="scroll flourish ornament"></span><span class="initials">E&amp;G</span><span class="flourish lower" role="img" aria-label="scroll flourish ornament"></span></div>
  <div class="crest" style="left:1080px;top:290px"><span class="flourish" role="img" aria-label="scroll flourish ornament"></span><span class="initials">E&amp;G</span><span class="flourish lower" role="img" aria-label="scroll flourish ornament"></span></div>
  <div class="crest" style="left:1080px;top:470px"><span class="flourish" role="img" aria-label="scroll flourish ornament"></span><span class="initials">E&amp;G</span><span class="flourish lower" role="img" aria-label="scroll flourish ornament"></span></div>
  <div class="crest" style="left:1080px;top:650px"><span class="flourish" role="img" aria-label="scroll flourish ornament"></span><span class="initials">E&amp;G</span><span class="flourish lower" role="img" aria-label="scroll flourish ornament"></span></div>
  <div class="crest" style="left:1080px;top:830px"><span class="flourish" role="img" aria-label="scroll flourish ornament"></span><span class="initials">E&amp;G</span><span class="flourish lower" role="img" aria-label="scroll flourish ornament"></span></div>
</main>
</body>
</html>
```